The Kelbridge Dog Stylist

I have a logo which I designed myself ( I tried a contest and it did not work out well..not on this site) The logo needs some tweaking for example "THE" needs to be put above "KELBRIDGE" in line with the D (on top)and it needs to be going across sideways.Also the dog is not exactly in the middle.
Also on the card I would like my name written in a simple running writing script
Margot

Then in plain writing:
17B Harlow St Kelbridge NSW 2795
Ph. 6391 5073
On the back:
Your next appointment:
...........................................

Pet bathing, clipping and styling

• The logo going across lengthways and changed a bit (as explained above)

```html
<!DOCTYPE html>
<html lang="en">
<head>
<meta charset="utf-8">
<title>The Kelbridge Dog Stylist – Business Card</title>
<link rel="stylesheet" href="https://fonts.googleapis.com/css2?family=Open+Sans:wght@400;600;700;800&display=swap">
<style>
  :root {
    --page: #ece8e3;
    --card: #ffffff;
    --ink: #111111;
    --red: #e0222b;
    --grey-text: #8a8a8a;
    --rule: #9a9a9a;
    --band: #0a0a0a;
    --band-text: #ffffff;
    --illustration: #dfe6ee;
    --illustration-deep: #b9c5d2;
  }

  * { box-sizing: border-box; margin: 0; padding: 0; }

  html, body {
    width: 1200px;
    height: 642px;
    overflow: hidden;
    background: var(--page);
    font-family: "Open Sans", Arial, sans-serif;
  }

  .sheet {
    position: relative;
    width: 1200px;
    height: 642px;
    display: flex;
    justify-content: center;
    align-items: center;
    gap: 40px;
  }

  .card {
    position: relative;
    width: 540px;
    height: 310px;
    background: var(--card);
    border-radius: 30px;
    overflow: hidden;
    box-shadow: 0 4px 14px rgba(0, 0, 0, 0.18);
  }

  .card__band {
    position: absolute;
    left: 0;
    right: 0;
    bottom: 0;
    height: 56px;
    background: var(--band);
    border-top: 5px solid var(--card);
    box-shadow: 0 -3px 0 var(--rule);
    display: flex;
    align-items: center;
    justify-content: center;
    color: var(--band-text);
    letter-spacing: 0.06em;
  }

  /* Front */
  .front__name {
    position: absolute;
    top: 20px;
    width: 100%;
    text-align: center;
    font-weight: 700;
    font-size: 26px;
    letter-spacing: 0.08em;
    color: var(--red);
  }

  .logo {
    position: absolute;
    top: 66px;
    left: 0;
    width: 100%;
    display: flex;
    align-items: center;
    justify-content: center;
    gap: 14px;
  }

  .logo__name {
    font-weight: 800;
    font-size: 27px;
    color: var(--ink);
    line-height: 1.05;
    text-align: right;
  }

  .logo__mascot {
    width: 92px;
    height: 92px;
    border-radius: 50%;
    background: radial-gradient(circle at 50% 45%, var(--illustration), var(--illustration-deep));
  }

  .front__phone {
    position: absolute;
    top: 184px;
    width: 100%;
    display: flex;
    align-items: center;
    justify-content: center;
    gap: 16px;
    font-weight: 700;
    font-size: 40px;
    line-height: 1;
    color: var(--red);
  }

  .front__phone svg { width: 32px; height: 32px; }

  .front__address { font-size: 18px; }

  /* Back */
  .appointment {
    position: absolute;
    top: 56px;
    left: 44px;
    color: var(--grey-text);
    font-size: 15px;
    line-height: 30px;
  }

  .appointment__field::after {
    content: " ..............................";
    letter-spacing: 0.02em;
  }

  .back__mascot {
    position: absolute;
    right: 30px;
    top: 62px;
    width: 150px;
    height: 180px;
    border-radius: 70px 70px 40px 40px;
    background: radial-gradient(circle at 50% 40%, var(--illustration), var(--illustration-deep));
  }

  .back__services { font-size: 15px; }
</style>
</head>
<body>
<main class="sheet">

  <section class="card card--front" aria-label="Card front">
    <p class="front__name">Margot</p>

    <div class="logo">
      <p class="logo__name">The Kelbridge<br>Dog Stylist</p>
      <div class="logo__mascot" role="img" aria-label="Cartoon white poodle illustration"></div>
    </div>

    <p class="front__phone">
      <svg viewBox="0 0 32 32" aria-hidden="true">
        <circle cx="16" cy="16" r="14" fill="none" stroke="#8a8a8a" stroke-width="2"/>
        <path d="M12 8.5c-1.6 0.6-2.6 2-2.3 3.8 0.8 4.6 4.4 9.2 8.8 11 1.7 0.7 3.3 0 4.2-1.4l-2.6-2.7-2 1c-2-1-3.6-3-4.4-5.2l1.7-1.4z" fill="#8a8a8a"/>
      </svg>
      6391 5073
    </p>

    <div class="card__band">
      <p class="front__address">17B Harlow St Kelbridge NSW 2795</p>
    </div>
  </section>

  <section class="card card--back" aria-label="Card back">
    <div class="appointment">
      <p>Your next appointment:</p>
      <p class="appointment__field">Date :</p>
      <p class="appointment__field">Day :</p>
      <p class="appointment__field">Time</p>
    </div>

    <div class="back__mascot" role="img" aria-label="Large cartoon white poodle illustration"></div>

    <div class="card__band">
      <p class="back__services">Pet Bathing, Clipping and Styling</p>
    </div>
  </section>

</main>
</body>
</html>
```